Software - upgrade look and feel

Brightmile Ledgerworks is the worldwide distributor of the uPlotta software application, which powers a loan strategy as described at www.brightmileledgerworks.com.The company has recently upgraded its image and website; and now seeks to give uPlotta a much-needed face-lift.Using the screen shots of the existing application (2 x screens provided), recreate the screens in a modern and vibrant style that generates a feeling of professionalism and confidence.
Updates

Project not yet launched and I felt 5 days was inadequate.

Target Market(s)

Financial services industry and their clients.

Industry/Entity Type

Financial Service

Font styles to use
Other font styles liked:
• See our website at brightmileledgerworks.com - happy with this font, but open to ideas.

Colors

Designer to choose colors to be used in the design.

Requirements
Must have
• Existing fields, but perhaps more intuitive for the User.
Nice to have
• A less busy look that suggests an innovative software application.
Should not have
• Complication.

```html
<!DOCTYPE html>
<html lang="en">
<head>
<meta charset="utf-8">
<title>uPlotta – Loan Strategy Screens</title>
<link href="https://fonts.googleapis.com/css2?family=Source+Sans+3:wght@400;600;700&display=swap" rel="stylesheet">
<style>
:root{
  --stage:#2c3a40;
  --panel:#efefef;
  --white:#ffffff;
  --teal:#1a93a9;
  --teal-dark:#0f6a86;
  --teal-deep:#0d5b74;
  --yellow:#fcd21f;
  --field:#e3e3e3;
  --field-text:#8a8a8a;
  --ink:#1e1e1e;
  --muted:#8c8c8c;
  --link:#1689a6;
  --cancel:#dcdcdc;
}
*{box-sizing:border-box;margin:0;padding:0}
html,body{width:930px;height:1200px;overflow:hidden;background:var(--stage);font-family:"Source Sans 3",sans-serif;color:var(--ink)}
.screen{position:absolute;left:30px;width:868px;height:548px;background:var(--panel);box-shadow:0 2px 10px rgba(0,0,0,.4)}
.screen--income{top:22px}
.screen--calculate{top:624px;height:546px}
.abs{position:absolute}
.tab-bar{position:absolute;left:0;top:0;width:868px;height:40px;background:linear-gradient(90deg,var(--teal-dark),var(--teal))}
.tab{position:absolute;top:0;height:40px;line-height:40px;color:var(--white);font-size:15px}
.tab--active{background:var(--panel);color:var(--link);padding-left:20px}
.tab-divider{position:absolute;top:8px;width:1px;height:26px;background:rgba(255,255,255,.35)}
.sub-tab{position:absolute;top:45px;font-size:15px;color:var(--muted)}
.sub-tab--active{color:var(--link)}
.details-bar{position:absolute;left:13px;top:83px;width:841px;height:26px;border:2px solid #a9b3b7;background:linear-gradient(90deg,var(--teal-deep),var(--teal));color:var(--white);font-size:11px;line-height:22px;padding:0 6px}
.details-bar .household{position:absolute;right:12px;top:0}
.card{position:absolute;background:var(--white)}
.label{position:absolute;font-size:12px;line-height:14px}
.link{position:absolute;font-size:11.5px;color:var(--link);text-decoration:underline}
.field{position:absolute;height:24px;background:var(--field);color:var(--field-text);font-size:11.5px;line-height:24px;padding-left:6px;white-space:nowrap;overflow:hidden}
.field--white{background:var(--white);color:var(--ink);border:1px solid #cfcfcf}
.spinner{position:absolute;width:23px;height:24px;background:var(--yellow)}
.spinner::before,.spinner::after{content:"";position:absolute;left:7px;border-left:4.5px solid transparent;border-right:4.5px solid transparent}
.spinner::before{top:4px;border-bottom:6px solid var(--white)}
.spinner::after{bottom:4px;border-top:6px solid var(--white)}
.info{position:absolute;width:14px;height:14px;border-radius:50%;background:var(--teal-dark);color:var(--white);font-size:10px;font-weight:700;line-height:14px;text-align:center}
.info--light{background:transparent;border:1.5px solid var(--white);line-height:11px}
.totals-band{position:absolute;left:13px;top:427px;width:840px;height:72px;background:linear-gradient(90deg,var(--teal-deep),var(--teal))}
.totals-label{position:absolute;right:193px;color:var(--white);font-size:11.5px;font-weight:600}
.btn{position:absolute;height:20px;border-radius:10px;font-size:12px;line-height:20px;text-align:center}
.btn--save{background:var(--yellow)}
.btn--cancel{background:var(--cancel)}
.radio{position:absolute;width:14px;height:14px;border-radius:50%;border:1.5px solid #c4c4c4;background:var(--white)}
.radio--on::after{content:"";position:absolute;left:3px;top:3px;width:5px;height:5px;border-radius:50%;background:var(--teal-dark)}
.savings{position:absolute;left:543px;top:390px;width:318px;height:114px;background:linear-gradient(90deg,var(--teal-deep),var(--teal-dark))}
.savings-label{position:absolute;left:13px;color:var(--white);font-size:11.5px;font-weight:700}
.savings .field{left:164px;width:144px;height:22px;line-height:22px}
</style>
</head>
<body>

<!-- Step 1: Client income -->
<section class="screen screen--income">
  <nav class="tab-bar">
    <div class="tab tab--active" style="left:0;width:186px">Step 1 - Client\Income</div>
    <div class="tab" style="left:206px">Step 2 - Expenses</div>
    <div class="tab-divider" style="left:335px"></div>
    <div class="tab" style="left:356px">Step 3 - Assets\Liabilities</div>
    <div class="tab-divider" style="left:529px"></div>
    <div class="tab" style="left:543px">Step 4 - Restructure</div>
    <div class="tab-divider" style="left:690px"></div>
    <div class="tab" style="left:714px">Step 5 - Calculate</div>
  </nav>
  <div class="sub-tab sub-tab--active" style="left:42px">Step 1 Quick</div>
  <div class="sub-tab" style="left:224px">Step 2 Quick</div>
  <div class="sub-tab" style="left:388px">Step 3 Quick</div>
  <div class="sub-tab" style="left:562px">Step 4 Quick</div>
  <div class="sub-tab" style="left:733px">Step 5 Quick</div>

  <div class="details-bar">Clients Details<span class="household">Tom &amp; Ellen Marsh</span></div>

  <div class="card" style="left:13px;top:114px;width:844px;height:92px"></div>
  <div class="label" style="left:17px;top:126px">View</div>
  <div class="link" style="left:14px;top:152px">Loan Writer User</div>
  <div class="link" style="left:14px;top:179px">CS Officer</div>
  <div class="info" style="left:117px;top:127px">i</div>
  <div class="field" style="left:140px;top:120px;width:136px">Client 1</div><div class="spinner" style="left:276px;top:120px"></div>
  <div class="field" style="left:140px;top:147px;width:136px">Hallett, Ray (552043817)</div><div class="spinner" style="left:276px;top:147px"></div>
  <div class="field" style="left:140px;top:174px;width:136px">Hallett, Ray (552043817)</div><div class="spinner" style="left:276px;top:174px"></div>
  <div class="label" style="left:322px;top:126px">Title</div>
  <div class="label" style="left:319px;top:154px">Family Name</div>
  <div class="label" style="left:322px;top:181px">First Name</div>
  <div class="info" style="left:398px;top:126px">i</div>
  <div class="info" style="left:398px;top:153px">i</div>
  <div class="info" style="left:398px;top:180px">i</div>
  <div class="field" style="left:426px;top:119px;width:55px"></div>
  <div class="field" style="left:426px;top:146px;width:154px">Marsh</div>
  <div class="field" style="left:426px;top:174px;width:154px">Tom</div>
  <div class="link" style="left:490px;top:126px">Additional Details</div>
  <div class="label" style="left:614px;top:127px">File No.</div>
  <div class="label" style="left:614px;top:153px">Email</div>
  <div class="info" style="left:683px;top:125px">i</div>
  <div class="info" style="left:683px;top:152px">i</div>
  <div class="field" style="left:707px;top:120px;width:144px">89923453-00001</div>
  <div class="field" style="left:707px;top:147px;width:144px"></div>
  <div class="link" style="left:614px;top:179px">Statistics</div>
  <div class="link" style="left:710px;top:180px">Send to Pending Tray</div>

  <div class="card" style="left:13px;top:216px;width:844px;height:205px"></div>
  <div class="label" style="left:140px;top:231px;font-weight:700;text-decoration:underline">Simulation Purpose</div>
  <div class="field" style="left:257px;top:224px;width:136px">Stragedy 1</div><div class="spinner" style="left:393px;top:224px"></div>
  <div class="link" style="left:433px;top:231px">Minimisation Stragedy</div>
  <div class="link" style="left:564px;top:231px">LBAA Guidelines</div>
  <div class="label" style="left:138px;top:260px;width:570px;font-weight:700">Please Enter the names of Client 1 and Client 2 (if applicable) then enter after tax wage of salary per frequency of payment.</div>
  <div class="label" style="left:229px;top:300px;font-size:11px">Net (After Tax)</div>
  <div class="label" style="left:403px;top:300px;font-size:11px">Freq. of Payment</div>
  <div class="label" style="left:138px;top:321px">Client 1</div>
  <div class="label" style="left:138px;top:351px">Client 2</div>
  <div class="field" style="left:224px;top:316px;width:154px">$1,000.00</div>
  <div class="field" style="left:224px;top:343px;width:154px">$1,500.00</div>
  <div class="field" style="left:399px;top:317px;width:155px">Weekly</div><div class="spinner" style="left:554px;top:317px"></div>
  <div class="field" style="left:399px;top:345px;width:155px">Fortnightly</div><div class="spinner" style="left:554px;top:345px"></div>
  <div class="label" style="left:138px;top:382px;width:580px">Note: Unless you enter the name of Client 1, no income will be saved for client 1.  Unless you enter Name of Client 2 , no income may be entered for Client 2.</div>

  <div class="totals-band">
    <div class="totals-label" style="top:14px">Client 1 After  Tax Income</div>
    <div class="totals-label" style="top:45px">Combiined After Tax Income</div>
    <div class="field field--white" style="left:665px;top:10px;width:155px">$52,000.00</div>
    <div class="field field--white" style="left:665px;top:37px;width:155px">$91,000.00</div>
  </div>

  <div class="card" style="left:13px;top:505px;width:844px;height:29px"></div>
  <div class="label" style="left:484px;top:513px;width:170px;text-align:right">Totals are Updated by clicking Save</div>
  <div class="btn btn--save" style="left:661px;top:510px;width:90px">Save</div>
  <div class="btn btn--cancel" style="left:757px;top:510px;width:88px">Cancel</div>
</section>

<!-- Step 5: Calculate -->
<section class="screen screen--calculate">
  <nav class="tab-bar">
    <div class="tab" style="left:21px">Step 1 - Client\Income</div>
    <div class="tab-divider" style="left:188px"></div>
    <div class="tab" style="left:206px">Step 2 - Expenses</div>
    <div class="tab-divider" style="left:335px"></div>
    <div class="tab" style="left:356px">Step 3 - Assets\Liabilities</div>
    <div class="tab-divider" style="left:529px"></div>
    <div class="tab" style="left:543px">Step 4 - Restructure</div>
    <div class="tab tab--active" style="left:690px;width:178px;padding-left:24px">Step 5 - Calculate</div>
  </nav>
  <div class="sub-tab" style="left:42px">Step 1 Quick</div>
  <div class="sub-tab" style="left:224px">Step 2 Quick</div>
  <div class="sub-tab" style="left:388px">Step 3 Quick</div>
  <div class="sub-tab" style="left:562px">Step 4 Quick</div>
  <div class="sub-tab sub-tab--active" style="left:733px">Step 5 Quick</div>

  <div class="details-bar">Clients Details<span class="household">Tom &amp; Ellen Marsh</span></div>

  <div class="card" style="left:13px;top:114px;width:844px;height:92px"></div>
  <div class="label" style="left:17px;top:126px">View</div>
  <div class="link" style="left:14px;top:152px">Loan Writer User</div>
  <div class="link" style="left:14px;top:179px">CS Officer</div>
  <div class="info" style="left:117px;top:127px">i</div>
  <div class="field" style="left:140px;top:120px;width:136px">Client 1</div><div class="spinner" style="left:276px;top:120px"></div>
  <div class="field" style="left:140px;top:147px;width:136px">Hallett, Ray (552043817)</div><div class="spinner" style="left:276px;top:147px"></div>
  <div class="field" style="left:140px;top:174px;width:136px">Hallett, Ray (552043817)</div><div class="spinner" style="left:276px;top:174px"></div>
  <div class="label" style="left:322px;top:126px">Title</div>
  <div class="label" style="left:319px;top:154px">Family Name</div>
  <div class="label" style="left:322px;top:181px">First Name</div>
  <div class="info" style="left:398px;top:126px">i</div>
  <div class="info" style="left:398px;top:153px">i</div>
  <div class="info" style="left:398px;top:180px">i</div>
  <div class="field" style="left:426px;top:119px;width:55px"></div>
  <div class="field" style="left:426px;top:146px;width:154px">Marsh</div>
  <div class="field" style="left:426px;top:174px;width:154px">Tom</div>
  <div class="link" style="left:490px;top:126px">Additional Details</div>
  <div class="label" style="left:614px;top:127px">File No.</div>
  <div class="label" style="left:614px;top:153px">Email</div>
  <div class="info" style="left:683px;top:125px">i</div>
  <div class="info" style="left:683px;top:152px">i</div>
  <div class="field" style="left:707px;top:120px;width:144px">89923453-00001</div>
  <div class="field" style="left:707px;top:147px;width:144px"></div>
  <div class="link" style="left:614px;top:179px">Statistics</div>
  <div class="link" style="left:710px;top:180px">Send to Pending Tray</div>

  <svg class="abs interest-chart" style="left:66px;top:232px" width="736" height="152" viewBox="0 0 736 152" role="img" aria-label="Area chart of loan balance over years, with and without extra payments">
    <polygon fill="#0f6a86" points="0,1.6 57,14.4 117,33.6 161,44 221,62.4 273,69.6 313,80 353,88 393,100 433,110 497,118 545,121.6 601,129.6 649,132 693,142.4 731,142.4 731,145.6 0,145.6"/>
    <polygon fill="#fcd21f" points="0,12 53,29.6 109,48 161,57.6 221,80 281,94.4 337,104 393,112 449,124 497,134 553,139 601,140.8 657,142.4 731,142.4 731,145.6 0,145.6"/>
    <line x1="0" y1="146" x2="731" y2="146" stroke="#b9b9b9" stroke-width="1"/>
    <line x1="0.5" y1="148" x2="731" y2="148" stroke="#b9b9b9" stroke-width="4" stroke-dasharray="1 5.6"/>
  </svg>

  <div class="card" style="left:12px;top:390px;width:531px;height:114px"></div>
  <div class="info" style="left:22px;top:402px">i</div>
  <div class="radio radio--on" style="left:53px;top:402px"></div>
  <div class="label" style="left:74px;top:402px">Graph - Years\Interest Saved</div>
  <div class="info" style="left:22px;top:472px">i</div>
  <div class="radio" style="left:53px;top:472px"></div>
  <div class="label" style="left:74px;top:472px">Loan Comparison</div>
  <div class="info" style="left:275px;top:402px">i</div>
  <div class="info" style="left:275px;top:426px">i</div>
  <div class="info" style="left:275px;top:450px">i</div>
  <div class="radio" style="left:299px;top:402px"></div>
  <div class="radio" style="left:299px;top:426px"></div>
  <div class="radio" style="left:299px;top:450px"></div>
  <div class="label" style="left:322px;top:402px">Analysis by Year</div>
  <div class="label" style="left:322px;top:426px">Analysis by Month</div>
  <div class="label" style="left:322px;top:450px">Analysis by Transaction:</div>
  <div class="field" style="left:298px;top:469px;width:136px">Step 4 Loans</div><div class="spinner" style="left:434px;top:469px"></div>

  <div class="savings">
    <div class="savings-label" style="top:12px">Potential Years Saved</div>
    <div class="savings-label" style="top:37px">Potencial Interest Save</div>
    <div class="savings-label" style="top:62px">Extra Payments Savings</div>
    <div class="savings-label" style="top:89px">Offset Savings</div>
    <div class="info info--light" style="left:143px;top:11px">i</div>
    <div class="info info--light" style="left:143px;top:36px">i</div>
    <div class="field" style="top:6px">7.00</div>
    <div class="field" style="top:32px">$105,336.33</div>
    <div class="field" style="top:60px">$101,629.50</div>
    <div class="field" style="top:87px">$3,706.83</div>
  </div>

  <div class="info" style="left:272px;top:518px">i</div>
  <div class="link" style="left:298px;top:519px">Report</div>
  <div class="card" style="left:645px;top:510px;width:214px;height:34px"></div>
  <div class="btn btn--save" style="left:663px;top:516px;width:89px">Save</div>
  <div class="btn btn--cancel" style="left:758px;top:516px;width:89px">Cancel</div>
</section>

</body>
</html>
```